Tend Your Harvest - Keep your Bloom - The freedom to choose and participate in your own path to hea

I have a logo that needs to be turned into a large banner for my website. I want to keep the same font in the uploaded logo image. Now this image could stay at the top of the header kind of where it is now on the web site, It doesn't have to be the main thing on the page. I want this header to be artistic - alive, healthy, joyous - colorful banner that shows wellness, healing, vitality and hope.
If you had a chronic illness and came to my site what would you want to see? You'd want to feel empowered, enlightened, engaged, hopeful and feel the love, right?.
I look forward to getting your creative ideas and designs.

Target Market(s)

People struggling with illness who are looking for a better quality of life. We provide training and education on how to do that. Hope, happiness - healing - Vitality - whole natural foods - mediation - visualization - whole health.

Industry/Entity Type

Health And Wellness

Logo Text

Tend Your Harvest with the koru and with Marigold Thwaite (use the font on the uploaded file)

Requirements
Must have
• I've changed the photos in this order. You can pick up options here:
• https://www.filebarrow.example/s/x7pleqnrtwz2kdm/IMG_4402%20%20high%20resolution.jpg?dl=0
• https://www.filebarrow.example/s/m3bvohqyeuc8zta/IMG_4587%20high%20resolution.jpg?dl=0
• My original logo - Tend Your Harvest - Marigold Thwaite
• "Together we make tragic moments magic moments" Join us (sign up type button)
Nice to have
• Something stunningly simple, classy, inviting, where my message gets across.
• Here's a similar website to mine: http://dalvenhope.example
• I need a link to join up somewhere - with my quote.
• "My tragic moments have become magic moments" Join us (sign up type button)
Should not have
• I do not want other people in the header.
• No crunchy granola feel!
• This is gone mainstream now.

```html
<!DOCTYPE html>
<html lang="en">
<head>
<meta charset="utf-8">
<title>Tend Your Harvest — Header Banner</title>
<link href="https://fonts.googleapis.com/css2?family=Quicksand:wght@500&family=Parisienne&family=Open+Sans:wght@400&display=swap" rel="stylesheet">
<style>
  :root {
    --canvas: #ffffff;
    --leaf-soft: #e6f2c8;
    --leaf-mid: #c9e29a;
    --leaf-deep: #9cc866;
    --portrait-warm: #d8b08a;
    --portrait-dark: #3b3835;
    --brand-teal: #5fb0b3;
    --script-gray: #7c7c7c;
    --accent-blue: #1fa3e0;
    --heart-blue: #35a8e6;
    --button-text: #ffffff;
  }
  * { margin: 0; padding: 0; box-sizing: border-box; }
  html, body { width: 1200px; height: 440px; overflow: hidden; background: var(--canvas); }

  .banner {
    position: relative;
    width: 1200px;
    height: 440px;
    overflow: hidden;
    background:
      radial-gradient(ellipse 140px 110px at 1120px 140px, var(--leaf-mid), transparent 75%),
      radial-gradient(ellipse 160px 120px at 1170px 250px, var(--leaf-soft), transparent 75%),
      radial-gradient(ellipse 220px 160px at 1000px 60px, #f1f7e4, transparent 80%),
      radial-gradient(ellipse 260px 180px at 1100px 420px, #eef6df, transparent 80%),
      radial-gradient(ellipse 300px 240px at 380px 220px, #f6f9ef, transparent 80%),
      var(--canvas);
  }

  .portrait {
    position: absolute;
    left: 0; top: 0;
    width: 430px; height: 440px;
    background:
      radial-gradient(ellipse 110px 150px at 150px 150px, var(--portrait-warm), transparent 80%),
      radial-gradient(ellipse 190px 200px at 200px 360px, var(--portrait-dark), transparent 80%),
      radial-gradient(ellipse 60px 120px at 20px 380px, var(--leaf-deep), transparent 80%),
      linear-gradient(90deg, #e9d7c2 0%, #efe4d6 60%, rgba(255,255,255,0) 100%);
    -webkit-mask-image: linear-gradient(90deg, #000 70%, transparent 100%);
            mask-image: linear-gradient(90deg, #000 70%, transparent 100%);
  }

  .brand {
    position: absolute;
    left: 706px; top: 14px;
    display: flex;
    align-items: center;
    gap: 10px;
    font-family: "Quicksand", sans-serif;
    font-weight: 500;
    color: var(--brand-teal);
  }
  .brand-dot {
    width: 22px; height: 22px;
    border-radius: 50%;
    background: var(--brand-teal);
    margin-top: 36px;
  }
  .brand-lines { display: flex; flex-direction: column; align-items: flex-end; }
  .brand-name { font-size: 26px; line-height: 34px; }
  .brand-person { font-size: 22px; line-height: 34px; }

  .quote {
    position: absolute;
    left: 600px; top: 168px;
    width: 540px; height: 140px;
    font-family: "Parisienne", cursive;
  }
  .quote-top, .quote-bottom { position: absolute; color: var(--script-gray); }
  .quote-top { left: 110px; top: 0; font-size: 34px; }
  .quote-main {
    position: absolute; left: 8px; top: 24px;
    font-size: 80px; line-height: 1;
    color: var(--accent-blue);
  }
  .quote-bottom { left: 72px; top: 92px; font-size: 36px; }
  .quote-close { left: 262px; top: 86px; font-size: 36px; }

  .join {
    position: absolute;
    left: 720px; top: 302px;
    width: 110px; height: 110px;
    display: block;
    text-decoration: none;
  }
  .join svg { position: absolute; inset: 0; }
  .join-label {
    position: absolute;
    left: 0; top: 40px; width: 104px;
    text-align: center;
    font-family: "Open Sans", sans-serif;
    font-size: 18px;
    color: var(--button-text);
  }
</style>
</head>
<body>
  <header class="banner">
    <div class="portrait" role="img" aria-label="Portrait photograph of the founder, smiling, in a dark jacket"></div>

    <div class="brand">
      <span class="brand-dot"></span>
      <div class="brand-lines">
        <span class="brand-name">Tend Your Harvest</span>
        <span class="brand-person">Marigold Thwaite</span>
      </div>
    </div>

    <div class="quote">
      <span class="quote-top">“Together we make</span>
      <span class="quote-main">tragic moments</span>
      <span class="quote-bottom">magic moments</span>
      <span class="quote-bottom quote-close">”</span>
    </div>

    <a class="join" href="#join">
      <svg width="110" height="110" viewBox="0 0 110 110" aria-hidden="true">
        <path d="M55 104 C30 84 4 64 4 36 C4 16 20 4 36 6 C46 7 52 14 55 22 C58 12 68 2 82 4 C98 6 108 20 104 40 C100 64 76 84 55 104 Z" fill="var(--heart-blue)"/>
      </svg>
      <span class="join-label">Join Us</span>
    </a>
  </header>
</body>
</html>
```